CupTradeHub

-
Below info still applicable but I wanted to highlight the point that I am looking for a design similar to the style linkloop+ with the mentioned color scheme (below). If you do that then the project is yours, I'm happy with an almost clone design. I know this is a completely different type of app but what I mean is:
- The listings to look like the linkloop+ widgets (i.e. blocks, three column, and clearly seperated)
- Adverts and listings mixed together in the results set
- Prominent listings to take up 2 or 3 of the columns instead, non prominent ones to take up 1.
- Clear spacing between the listings, as with linkloop+ widgets
- Clear seperation between menu and widgets as with linkloop+
- Search/filters and category filters on the right or left, as with linkloop+
Again, if this is not clear I want it LIKE LINKLOOP+, so far had stock template designs that weren't anything like this.
Linkloop+ is not the only site I listed for inspiration, but I think its easier at this point to just say clone the damn thing, and re purpose it for coffee. We will make additional changes at development time to make it distinct and incorporate some of the other things we were looking for.
-
Hi All,
I'm looking to get designs for a new site that allows coffee roasters, and barista equipment suppliers to sell their goods to coffee shops via an auction site. So essentially B2B bidnest targeted at the coffee market.
Pages required:
All pages:
- Logo
- Login/register links (or my account if logged in)
- links to Contact us, FAQs, Advertise with us
Homepage:
- Search bar
- List of filter categories
- Latest products section
- Advertising section
Search page:
- Listings (Image, price (buy now or current bid), postage price, no bids, time remaining to bid)
- Advertising
Listing page
- Same listing info as above but with full description, multipule images to select from, time ending and and a bid form (enter amount) or buy now button.
Login page
- Username/Password
- Alternative login via Friendora
My account:
- Link to add listings
- List of current listings
- List of current bids
- Link to purchase history
Add a listing:
- Form page to add a listing
- Requires
- Images uploads (drag to upload, as well as normal)
- Title field
- Description field
- Amount field
- Quantity field
- Postage amount field
- Category Drop down field
- End date/time picker field
That's it for functionality, with regards to design this needs to be designed in a way that is compatible with scaffoldr components (http://chirpnet.codehost.example/scaffoldr/), though scaffoldr is highly customizable so don't feel too restricted.
Styles/colours:
Site layout should be clean, and clear utilizing white space well i.e.
- http://shrt.example/qpWmT
- http://shrt.example/VbRdK
- https://circles.linkloop.example/
Also VERY much like the vantasoft "tiler" style design i.e. square boxes. If you know what I mean by this then cool, if not don't worry about it.
The logo on the other hand should have and earthy, organic feel to it.
Also, please only use fonts available from typevault fonts (http://www.typevault.example/fonts/).

```html
<!DOCTYPE html>
<html lang="en">
<head>
<meta charset="utf-8">
<title>CupTradeHub</title>
<link href="https://fonts.googleapis.com/css2?family=Ubuntu:wght@400;500&family=Oswald:wght@300&display=swap" rel="stylesheet">
<style>
:root{
  --khaki:#d9cd9a;
  --khaki-light:#e9e0b8;
  --espresso:#3a1709;
  --espresso-deep:#2f1408;
  --teal:#12917f;
  --caramel:#a0581f;
  --tan-box:#d8c88c;
  --tan-text:#9a8440;
  --grey-text:#8a8a8a;
  --line:#e3e3e3;
  --cream:#efe6bd;
}
*{box-sizing:border-box;margin:0;padding:0}
html,body{width:1200px;height:911px;overflow:hidden;background:#fff;font-family:"Ubuntu",sans-serif}
.page{position:relative;width:1200px;height:911px;overflow:hidden}

.topbar{position:absolute;left:0;top:0;width:1200px;height:38px;background:linear-gradient(#e2d8aa,var(--khaki));box-shadow:0 1px 3px rgba(0,0,0,.15)}
.brand{position:absolute;left:283px;top:9px;display:flex;align-items:center;gap:6px;color:var(--espresso);font-size:17px;font-weight:500;letter-spacing:.2px}
.brand-dot{width:14px;height:18px;border-radius:50%;background:var(--caramel)}
.account{position:absolute;right:288px;top:11px;display:flex;gap:8px}
.account a{display:block;height:18px;padding:0 9px;line-height:18px;font-size:8.5px;color:#fff;text-decoration:none;background:var(--espresso);border-radius:2px;box-shadow:0 1px 2px rgba(0,0,0,.3)}

.menu{position:absolute;left:288px;top:53px;display:flex;height:20px;box-shadow:0 1px 2px rgba(0,0,0,.12)}
.menu a{display:block;padding:0 12px;line-height:20px;font-size:8px;color:var(--grey-text);text-decoration:none;border-right:1px solid var(--line);background:#fff}
.menu a.active{background:var(--espresso);color:#fff;padding:0 16px}
.search{position:absolute;left:727px;top:53px;width:186px;height:20px;display:flex;border:1px solid var(--line)}
.search span{flex:1;font-size:7.5px;color:#999;line-height:18px;padding-left:6px}
.search i{width:20px;background:var(--espresso);position:relative}
.search i::before{content:"";position:absolute;left:5px;top:4px;width:6px;height:6px;border:1.5px solid #fff;border-radius:50%}
.search i::after{content:"";position:absolute;left:12px;top:11px;width:4px;height:1.5px;background:#fff;transform:rotate(45deg)}

.listings{position:absolute;left:288px;top:87px;display:grid;grid-template-columns:repeat(4,148px);column-gap:11px;row-gap:12px}
.card{position:relative;width:148px;height:263px;background:#fff;box-shadow:0 0 3px rgba(0,0,0,.18)}
.card-photo{position:absolute;left:22px;top:12px;width:104px;height:106px;border-radius:6px;background:radial-gradient(circle at 50% 45%,#5b5550,#b9b6b2 60%,#fff 80%)}
.bid{position:absolute;right:0;top:133px;width:76px;height:19px;background:var(--espresso-deep);color:#fff;font-size:9px;text-align:center;line-height:19px}
.card-title{position:absolute;left:0;top:160px;width:148px;height:24px;background:var(--teal);color:#fff;font-size:9.5px;line-height:24px;padding-left:6px;white-space:nowrap;overflow:hidden}
.timer{position:absolute;left:19px;top:192px;display:flex;gap:5px}
.unit{text-align:center;width:32px}
.unit b{display:block;height:26px;border-radius:3px;background:linear-gradient(#e5d9a5,var(--tan-box));color:var(--espresso);font-size:12px;font-weight:500;line-height:26px}
.unit small{display:block;font-size:7px;color:var(--tan-text);margin-top:2px}
.likes{position:absolute;left:6px;right:0;bottom:0;height:24px;border-top:1px dotted #ccc;font-family:"Oswald",sans-serif;font-size:7.5px;color:var(--grey-text);line-height:24px}
.likes-count{position:absolute;right:0;bottom:0;width:40px;height:40px;background:linear-gradient(135deg,transparent 50%,var(--caramel) 50%);color:#fff;font-family:"Ubuntu",sans-serif;font-size:7.5px}
.likes-count span{position:absolute;right:5px;bottom:3px;line-height:1}
.likes-count svg{position:absolute;right:8px;top:17px}

.loading{position:absolute;left:580px;top:646px;width:80px;text-align:center;color:var(--tan-box);font-size:11px;letter-spacing:.5px}
.loading svg{display:block;margin:0 auto 6px}

.art-left{position:absolute;left:48px;top:358px;width:236px;height:352px;background:radial-gradient(ellipse at 45% 60%,rgba(160,88,31,.35),rgba(255,255,255,0) 70%)}
.art-right{position:absolute;left:930px;top:580px;width:230px;height:160px;background:radial-gradient(ellipse at 55% 65%,rgba(90,45,20,.45),rgba(255,255,255,0) 70%)}

.footer{position:absolute;left:0;top:718px;width:1200px;height:193px}
.footer-edge{position:absolute;left:0;top:0}
.footer-body{position:absolute;left:0;top:30px;width:1200px;height:163px;background:var(--espresso-deep)}
.fcol{position:absolute;top:52px}
.fcol h3{font-size:12.5px;font-weight:400;color:var(--cream);margin-bottom:8px}
.f-about{left:285px;width:192px}
.f-about h3{display:flex;align-items:center;gap:6px}
.f-about h3 i{width:10px;height:14px;border-radius:50%;background:var(--caramel)}
.f-about p{font-size:7px;line-height:12px;color:var(--khaki)}
.f-company{left:515px}
.f-company a{display:block;font-size:7.5px;line-height:12px;color:var(--cream);text-decoration:none}
.f-mail{left:637px}
.f-mail p{font-size:7.5px;color:var(--cream);margin-bottom:6px}
.f-mail .field{width:142px;height:21px;background:var(--caramel);margin-bottom:10px}
.f-mail .btn{width:70px;height:21px;background:var(--tan-box);color:var(--espresso);font-size:9px;text-align:center;line-height:21px}
.f-follow{left:817px}
.f-follow p{font-size:7px;line-height:11px;color:var(--caramel)}
.divider{position:absolute;top:55px;width:1px;height:84px;background:#4a2414}
.copyright{position:absolute;left:285px;top:161px;font-size:7.5px;color:var(--caramel)}
</style>
</head>
<body>
<div class="page">
  <header class="topbar">
    <div class="brand"><i class="brand-dot"></i>CUPTRADEHUB</div>
    <nav class="account">
      <a href="#">Connect To Friendora</a><a href="#">REGISTER</a><a href="#">LOGIN</a>
    </nav>
  </header>

  <nav class="menu">
    <a class="active" href="#">Popular</a><a href="#">Recent</a><a href="#">Advertise With Us</a><a href="#">Contact Us</a><a href="#">Categories</a><a href="#">FAQ'S</a>
  </nav>
  <div class="search"><span>Enter Your Keywords Here...</span><i></i></div>

  <div class="art-left" role="img" aria-label="Illustration of coffee beans and a steaming cup drawn in brown lines"></div>
  <div class="art-right" role="img" aria-label="Photo of coffee beans beside a white espresso cup with steam"></div>

  <main class="listings">
    <article class="card"><div class="card-photo" role="img" aria-label="Photo of an espresso grinder"></div><div class="bid">Bid Now!</div><h2 class="card-title">Barista-Espresso-Grinder</h2><div class="timer"><div class="unit"><b>02</b><small>Hours</small></div><div class="unit"><b>07</b><small>Minutes</small></div><div class="unit"><b>16</b><small>Seconds</small></div></div><div class="likes">LIKES THIS<div class="likes-count"><svg width="7" height="6" viewBox="0 0 10 9"><path d="M5 9 0 4A2.5 2.5 0 0 1 5 1a2.5 2.5 0 0 1 5 3z" fill="#fff"/></svg><span>320</span></div></div></article>
    <article class="card"><div class="card-photo" role="img" aria-label="Photo of a black coffee machine"></div><div class="bid">Bid Now!</div><h2 class="card-title">Making Coffee</h2><div class="timer"><div class="unit"><b>02</b><small>Hours</small></div><div class="unit"><b>07</b><small>Minutes</small></div><div class="unit"><b>16</b><small>Seconds</small></div></div><div class="likes">LIKES THIS<div class="likes-count"><svg width="7" height="6" viewBox="0 0 10 9"><path d="M5 9 0 4A2.5 2.5 0 0 1 5 1a2.5 2.5 0 0 1 5 3z" fill="#fff"/></svg><span>102</span></div></div></article>
    <article class="card"><div class="card-photo" role="img" aria-label="Photo of a steel espresso machine"></div><div class="bid">Bid Now!</div><h2 class="card-title">The Crema Express</h2><div class="timer"><div class="unit"><b>02</b><small>Hours</small></div><div class="unit"><b>07</b><small>Minutes</small></div><div class="unit"><b>16</b><small>Seconds</small></div></div><div class="likes">LIKES THIS<div class="likes-count"><svg width="7" height="6" viewBox="0 0 10 9"><path d="M5 9 0 4A2.5 2.5 0 0 1 5 1a2.5 2.5 0 0 1 5 3z" fill="#fff"/></svg><span>325</span></div></div></article>
    <article class="card"><div class="card-photo" role="img" aria-label="Photo of a red coffee grinder"></div><div class="bid">Bid Now!</div><h2 class="card-title">m40-Coffee-Grinder</h2><div class="timer"><div class="unit"><b>02</b><small>Hours</small></div><div class="unit"><b>07</b><small>Minutes</small></div><div class="unit"><b>16</b><small>Seconds</small></div></div><div class="likes">LIKES THIS<div class="likes-count"><svg width="7" height="6" viewBox="0 0 10 9"><path d="M5 9 0 4A2.5 2.5 0 0 1 5 1a2.5 2.5 0 0 1 5 3z" fill="#fff"/></svg><span>136</span></div></div></article>
    <article class="card"><div class="card-photo" role="img" aria-label="Photo of a domestic capsule coffee machine"></div><div class="bid">Bid Now!</div><h2 class="card-title">Domestic Coffee Machines</h2><div class="timer"><div class="unit"><b>02</b><small>Hours</small></div><div class="unit"><b>07</b><small>Minutes</small></div><div class="unit"><b>16</b><small>Seconds</small></div></div><div class="likes">LIKES THIS<div class="likes-count"><svg width="7" height="6" viewBox="0 0 10 9"><path d="M5 9 0 4A2.5 2.5 0 0 1 5 1a2.5 2.5 0 0 1 5 3z" fill="#fff"/></svg><span>146</span></div></div></article>
    <article class="card"><div class="card-photo" role="img" aria-label="Photo of a filter coffee maker with glass jug"></div><div class="bid">Bid Now!</div><h2 class="card-title">Rivolo Filter Coffee Maker</h2><div class="timer"><div class="unit"><b>02</b><small>Hours</small></div><div class="unit"><b>07</b><small>Minutes</small></div><div class="unit"><b>16</b><small>Seconds</small></div></div><div class="likes">LIKES THIS<div class="likes-count"><svg width="7" height="6" viewBox="0 0 10 9"><path d="M5 9 0 4A2.5 2.5 0 0 1 5 1a2.5 2.5 0 0 1 5 3z" fill="#fff"/></svg><span>564</span></div></div></article>
    <article class="card"><div class="card-photo" role="img" aria-label="Photo of a bean-to-cup coffee machine"></div><div class="bid">Bid Now!</div><h2 class="card-title">Bean-to-cup coffee</h2><div class="timer"><div class="unit"><b>02</b><small>Hours</small></div><div class="unit"><b>07</b><small>Minutes</small></div><div class="unit"><b>16</b><small>Seconds</small></div></div><div class="likes">LIKES THIS<div class="likes-count"><svg width="7" height="6" viewBox="0 0 10 9"><path d="M5 9 0 4A2.5 2.5 0 0 1 5 1a2.5 2.5 0 0 1 5 3z" fill="#fff"/></svg><span>678</span></div></div></article>
    <article class="card"><div class="card-photo" role="img" aria-label="Photo of a silver automatic coffee centre with latte glasses"></div><div class="bid">Bid Now!</div><h2 class="card-title">VELA XC GRANDE</h2><div class="timer"><div class="unit"><b>02</b><small>Hours</small></div><div class="unit"><b>07</b><small>Minutes</small></div><div class="unit"><b>16</b><small>Seconds</small></div></div><div class="likes">LIKES THIS<div class="likes-count"><svg width="7" height="6" viewBox="0 0 10 9"><path d="M5 9 0 4A2.5 2.5 0 0 1 5 1a2.5 2.5 0 0 1 5 3z" fill="#fff"/></svg><span>452</span></div></div></article>
  </main>

  <div class="loading">
    <svg width="40" height="40" viewBox="-20 -20 40 40">
      <g stroke="#d8c88c" stroke-width="3" stroke-linecap="round">
        <line x1="0" y1="-9" x2="0" y2="-18"/><line x1="0" y1="-9" x2="0" y2="-18" transform="rotate(30)"/><line x1="0" y1="-9" x2="0" y2="-18" transform="rotate(60)"/><line x1="0" y1="-9" x2="0" y2="-18" transform="rotate(90)"/><line x1="0" y1="-9" x2="0" y2="-18" transform="rotate(120)"/><line x1="0" y1="-9" x2="0" y2="-18" transform="rotate(150)"/><line x1="0" y1="-9" x2="0" y2="-18" transform="rotate(180)"/><line x1="0" y1="-9" x2="0" y2="-18" transform="rotate(210)"/><line x1="0" y1="-9" x2="0" y2="-18" transform="rotate(240)"/><line x1="0" y1="-9" x2="0" y2="-18" transform="rotate(270)"/><line x1="0" y1="-9" x2="0" y2="-18" transform="rotate(300)"/><line x1="0" y1="-9" x2="0" y2="-18" transform="rotate(330)"/>
      </g>
    </svg>
    LOADING
  </div>

  <footer class="footer">
    <svg class="footer-edge" width="1200" height="32" viewBox="0 0 1200 32" preserveAspectRatio="none">
      <path d="M0 14 30 10 70 13 120 8 170 12 230 9 300 13 360 8 430 12 500 9 560 13 640 8 700 12 770 9 840 13 900 8 970 12 1040 9 1110 13 1160 9 1200 12V32H0Z" fill="#e6d9a2"/>
      <path d="M0 20 40 17 90 21 150 16 210 20 270 17 340 21 400 16 470 20 540 17 600 21 670 16 740 20 810 17 880 21 950 16 1020 20 1090 17 1150 21 1200 18V32H0Z" fill="#8a4a1d"/>
      <path d="M0 26 60 24 130 27 200 24 280 27 350 24 430 27 510 24 590 27 670 24 750 27 830 24 910 27 990 24 1070 27 1140 24 1200 26V32H0Z" fill="#2f1408"/>
    </svg>
    <div class="footer-body"></div>
    <section class="fcol f-about">
      <h3><i></i>CUPTRADEHUB</h3>
      <p>Lorem ipsum dolor sit amet, consectetuer adipiscing elit, sed diam nonummy nibh euismod tincidunt ut laoreet dolore magna aliquam erat volutpat. Ut wisi enim ad minim veniam, quis nostrud exerci tation ullamcorper suscipit lobortis nisl ut aliquip ex ea commodo consequat.</p>
    </section>
    <div class="divider" style="left:489px"></div>
    <section class="fcol f-company">
      <h3>COMPANY</h3>
      <a href="#">About</a><a href="#">FAQ</a><a href="#">Contact</a><a href="#">Advertise With Us</a><a href="#">Privacy</a>
    </section>
    <div class="divider" style="left:620px"></div>
    <section class="fcol f-mail" style="top:50px">
      <h3>JOIN OUR MAILING LIST</h3>
      <p>Subscribe to Free Promotions</p>
      <div class="field"></div>
      <div class="btn">Subscribe</div>
    </section>
    <div class="divider" style="left:793px"></div>
    <section class="fcol f-follow" style="top:50px">
      <h3>FOLLOW US</h3>
      <p>Friendora · Chirpnet<br>Linkloop+ · Pinboardly<br>Dotshot</p>
    </section>
    <p class="copyright">© 2013 CUPTRADEHUB.com. All Rights Reserved.</p>
  </footer>
</div>
</body>
</html>
```